Sophisticated & Clean Comedy Show Flyer

Pale Harbor Entertainment, a talent management company, is producing a showcase to introduce their comedians to the industry. The design should be clean and sophisticated and introduce a graphical element that evokes comedy, without being cheesy.

I have attached the following files:
* Pale Harbor Logo - file #1
* Copy for flyer - file #2
* textured business card for Pale Harbor Entertainment for design reference - file #3
* example of a comedy flyer with graphic and texture that is clean and sophisticated and fun. - file #4

Industry/Entity Type

Entertainment Industry

Font styles to use
Sans Serif

Colors
000000
ffffff
e8e8e8

Requirements
Must have
• Logo ad all the content listed in the file #2
Nice to have
• A graphical element that evokes comedy that is not generic or cheesy
• I don't mind accent color on the flyer - but overall it should be clean look

```html
<!DOCTYPE html>
<html lang="en">
<head>
<meta charset="utf-8">
<title>Pale Harbor Entertainment Comedy Showcase</title>
<link href="https://fonts.googleapis.com/css2?family=Archivo+Narrow:wght@400;700&display=swap" rel="stylesheet">
<style>
  :root {
    --ink: #000000;
    --paper: #ffffff;
    --mist: #e8e8e8;
  }
  html, body {
    margin: 0;
    padding: 0;
    overflow: hidden;
    background: var(--ink);
  }
  .flyer {
    position: relative;
    width: 849px;
    height: 1200px;
    overflow: hidden;
    background: radial-gradient(ellipse at 40% 40%, #1c1c1c 0%, var(--ink) 70%);
    color: var(--paper);
    font-family: "Archivo Narrow", "Arial Narrow", sans-serif;
  }
  .brand {
    position: absolute;
    left: 240px;
    top: 14px;
    width: 380px;
    height: 118px;
    background: var(--paper);
    color: var(--ink);
    display: flex;
    flex-direction: column;
    align-items: center;
    justify-content: center;
    font-weight: 700;
    text-transform: uppercase;
    line-height: 1;
  }
  .brand-name { font-size: 54px; letter-spacing: 1px; }
  .brand-sub { font-size: 22px; letter-spacing: 3px; margin-top: 6px; }
  .event-title {
    position: absolute;
    top: 152px;
    left: 0;
    width: 849px;
    text-align: center;
    font-size: 46px;
    font-weight: 700;
    letter-spacing: 1px;
    margin: 0;
    line-height: 1;
  }
  .portrait {
    position: absolute;
    left: 100px;
    top: 215px;
    width: 470px;
    height: 550px;
    border-radius: 46% 50% 44% 50%;
    background: radial-gradient(ellipse at 45% 45%, #6e6e6e 0%, #3c3c3c 45%, rgba(20,20,20,0) 75%);
  }
  .host {
    position: absolute;
    left: 436px;
    top: 572px;
    width: 260px;
    margin: 0;
    text-align: center;
    font-size: 21px;
    line-height: 24px;
    color: var(--mist);
    z-index: 2;
  }
  .host strong { display: block; font-size: 22px; color: var(--paper); }
  .date-badge {
    position: absolute;
    left: 400px;
    top: 654px;
    width: 376px;
    height: 356px;
    border-radius: 50%;
    background: var(--paper);
    color: var(--ink);
    display: flex;
    flex-direction: column;
    align-items: center;
    justify-content: center;
    text-align: center;
  }
  .date-day { font-size: 84px; font-weight: 700; line-height: 1; }
  .date-month { font-size: 50px; font-weight: 400; line-height: 1.1; }
  .date-times { font-size: 17px; margin-top: 40px; }
  .lineup {
    position: absolute;
    left: 28px;
    top: 958px;
    font-size: 25px;
    line-height: 29px;
    text-transform: uppercase;
  }
  .lineup-label { text-transform: none; }
  .lineup ul { list-style: none; margin: 0; padding: 0; }
  .lineup .credit { text-transform: none; }
  .venue {
    position: absolute;
    left: 28px;
    top: 1146px;
    font-size: 25px;
    line-height: 29px;
    text-transform: uppercase;
  }
</style>
</head>
<body>
<main class="flyer">
  <header class="brand">
    <span class="brand-name">Pale Harbor</span>
    <span class="brand-sub">Entertainment</span>
  </header>
  <h1 class="event-title">COMEDY SHOWCASE</h1>

  <div class="portrait" role="img" aria-label="Textured charcoal portrait of a laughing comedian"></div>

  <p class="host">Hosted by<strong>RUDY VANCE HOLLISTER</strong>(Laugh Channel)</p>

  <section class="date-badge">
    <div class="date-day">MONDAY,</div>
    <div class="date-month">NOVEMBER 16th</div>
    <div class="date-times">Doors 7PM &nbsp;Show 7:30PM</div>
  </section>

  <section class="lineup">
    <div class="lineup-label">Featuring</div>
    <ul>
      <li>Dana Whitlock <span class="credit">(Laugh Channel, Loop TV)</span></li>
      <li>Marcus Delaney <span class="credit">(Vista TV, Beacon)</span></li>
      <li>Tobias Renard <span class="credit">(Vista TV)</span></li>
      <li>Lena Marsh <span class="credit">(Harborline, Vista TV)</span></li>
      <li>Owen Kessler <span class="credit">(Eastside Comedy Festival)</span></li>
    </ul>
  </section>

  <footer class="venue">Larkspur 318 W 19th Street, NY, NY 10014</footer>
</main>
</body>
</html>
```